Coastal Banner Bridge website for creative design and functionality.

Using Wordpress and creative license, create an exciting attractive and super interesting website concept that is easy to navigate, educational, fun, youthful, funny, colourful, global, appealing to all age groups and most businesses who have a use for SIGNS.
Products offered are electronic signs, illuminated channel letters, non-illuminated flat cut and molded letters, specialty products, Wayfinding, large format digital printing, volume printing, programs, rebranding, illuminated cabinet type signs and illuminated freestanding signs.
Services include design (to which ArtHiveHub could be a link), surveys, permits, installations and maintenance.
National refers to CANADA although USA clients who have requirements in Canada or Canadian clients having requirements in the USA are welcome.
Degree of difficulty here is well appreciated. Winner will be selected on basis of creative appeal and uniqueness as well as the designer being able and willing to provide a turnkey service to get the site up and running with or without the help of a lead website designer in Canada.
Domain is coastalbannerbridge.ca primary and coastalbannerbridge.com secondary.
Logo exists. Flow chart concept exists. Intent outline exists.
Site should include galleries, Q & A, ugly or funny signs international encouraging global participation, monitored forum for praise and constructive criticism.
CBB works for the client. Objective is to provide premium quality products of ALL TYPES anywhere, for less than market value, from recognized industry leaders (Links), in a timely manner, with transparency, integrity.
Concept is not new but the difference is degree of honesty, commitment to best value, truthfulness of the statement that 'we work for you'.
Given the challenge of website design, we recognize that a turnkey solution can cost us thousands. In an effort to be consistent with our high client standards, we also intend to be extremely loyal and honest and appreciative of the competition winner over the long term as well as anyone who 'tied' or came close second.
To this end, we feel that $500.00 US is a fair incentive to a competition winner whose 'brainchild' is used in whole or in part with two revisions. To be fair to ourselves, we would not be expected to pay anything if the competition generates nothing that excites us. We will work with ArtHiveHub to define that.
As with our future clients, we will be fair, not greedy and honest in our dealings with vendors including designers who want to work with us moving forward. Your excitement will show in your work. Hopefully, our excitement is evident and contagious.
It is not in our best interest nor Arthivehub's best interest to make the contest entries public information due to what we perceive as being a unique competitive template to virtual sign supply. It is suggested that promotion of the creative material produced by entrants be limited to the home page and not the detailed inner 'beauty' of the concept.
I will provide all competitors with all answers to any questions that come up so that a fair playing field is created.
Thank You,
Tom

Target Market(s)

See general info below

Number of Pages Required

5+ page

Font styles to use
Sans Serif

Requirements
Must have
• Defining your business
• 1. Who is your target market?
• Target market is National, Regional and Local entities who buy signs. Targets are retailers, developers, project managers landlords, marketing personnel, Architects, designers and builder.
• 2. What is the overall purpose of your business?
• To do a better job than the conventional sign shop. Better response, better pricing, better communication, better value.
• 3. What distinguishes you from your competitors?
• CBB does not manufacture. We rely on experienced ‘Links’ to provide quality products, preproduction services like surveys and permits, field services like installation and service.
• 4. Who are your major competitors?
• All sign manufacturers are our competitors. Major competitors are those who do multiple locations or program selling. That said, most sign companies have such accounts. Our Links are also our competitors to some degree although we would respect their relationship under normal conditions.
• 6. What are 3 of your businesses strengths?
• Industry relationships (links), knowledge (25 and 40 years of industry experience respectively), existing contact lists of potential clients
• 7. What are the top 3 business values? We work for the client and pride ourselves on our honesty, transparency and integrity
• 8. Do you have a mission statement? If so please include.
• 9. What is your primary offering?
• Illuminated and non-illuminated channel letters, non-illuminated flat cut and molded and specialty letters, electronic signs, large format digital printing. Freestanding signs, illuminated and non-illuminated cabinet signs (wall signs)
• 10. What is your second offering?
• Design, survey, permits, installation and service and to be treated
• 11. What do your customers want?
• Customers want to be treated fairly. They want to be informed and involved (good communications). They want products on time and on budget and right the first time.
• 12. What is the “Emotional Appeal” you want to establish? The feeling you want to come across. In your text, images and graphics?
• Relaxed, excitement, comfort, calm, humour, seriousness, educational, health , confidence, professionalism, knowledgeable
• Marketing and establishing your brand?
• Brand + Marketing + Consistency = CUSTOMERS
• 1. What are some images that best reflect your company brand? ( list three or more)
• Professional. Knowledgeable, loyal, trustworthy, new, positive, confident, artistic, talented, devoted
• 2. What are some colors that best represent your company?
• Multi-color images with pizzaz. Back for nighttime, white for daytime, red for Canadian
• 3. What is your tagline? If you don’t have a tagline please keep these points in mind when creating a tagline. a. Make it quick and easy to say
• b. Try not to go beyond six words. (little words like “the“, and “and” don’t count)
• c. Something that rolls of your tongue and straight into your customer’s memory.
• d. Make sure it provides information.
• COASTAL BANNER BRIDGE WHERE EXPERIENCE COMES TOGETHER
• Creating your Website
• Please keep in mind that a website can be done in stages. Not everything has to be done before your website goes live. You can add details and blogs, and newsletters as you see fit. Please indicate whether you will need any of these items now or in the future phases of your site.
• 1. Home page think “HOOK” your home page is everything and it’s critical that you instantly hook visitors. Don’t rule out Q&A, the promise of freebies or interesting tips.
• Yes. I want Q & A, ugly and interesting sign gallery from public input, occasional time limited specials for supply of product
• 2. Will you be writing your own content or provide information for us to write it?
• We will work together to create content that we both feel is perfect
• 3. If you are writing your own content will you have someone proof read and edit your content for search engine optimization or will you need us to perform that task?
• You two
• 4. Will you need PayPal on your website?
• No. I have credit card payment capability on our invoices.
• 5. How often will your website need to be updated?
• Weekly hopefully
• 6. Are you thinking of updating your own website?
• Yes
• 7. Will you need a log in account with passwords set up for each customer?
• No
• 8. Will you need a newsletter program for promotions and valuable information? (remember these take time and skill)
• No
• 9. Will you be blogging? (do you have enough information to continue weekly or monthly)
• I don’t think so. I would like to use the Q & A format for that if possible
• 10. How many email accounts will you need to have set up?
• Four should be fine. Two at first
• 11. Will there be any forms on your site and if so how many?
• Quote request form on each product page. Custom order form on Orchid page and maybe the channel letter depot page. We will need a form for submission of photos and artwork (drop box) with file types defined. Design request form with fee schedule
• 12. Will there be a photo gallery and if so how many?
• Yes and several. One for each product. One for for ugly and funny. One for completed CBB projects. Eight to ten.
• 13. Will you need an appointment program for clients to make appointments?
• Yes.
• 14. Do you have a logo?
• Yes
• 15. Do you have an existing website?
• No
• 16. Do you have existing marketing material?
• No BUT each product link (wholesalers) have marketing material and we have permission to use their site content. Eg. Pavo catalog can be downloaded and printed.
• ’
• I do like the static header where viewer has the logo and menu in front of them no matter where they are on the site.
• I don’t like the ‘hamburger’ icon for menu selection – something more personal.
• I like a welcoming atmosphere. Hello. Welcome.
• I would like a glossary of terms page
• Definitely want to encourage ANY questions from ANYBODY that we can respond to with or without research and hence develop and promote FAQ
Nice to have
• See must haves

```html
<!DOCTYPE html>
<html lang="en">
<head>
<meta charset="utf-8">
<title>Coastal Banner Bridge</title>
<link rel="stylesheet" href="https://fonts.googleapis.com/css2?family=Lato:wght@400;700&family=Roboto:wght@400;500&family=Roboto+Condensed:wght@500;700&family=Open+Sans:wght@400;600&display=swap">
<style>
  :root {
    --navy: #173a6e;
    --navy-deep: #0f2f60;
    --band-top: #1a4482;
    --band-bottom: #0b2856;
    --ink: #2b2b2b;
    --muted: #4a4a4a;
    --white: #ffffff;
    --footer-bg: #f1f1f1;
    --rule: #d6d6d6;
  }
  * { margin: 0; padding: 0; box-sizing: border-box; }
  html, body { width: 1200px; height: 2795px; overflow: hidden; }
  body { position: relative; background: var(--white); font-family: "Open Sans", Arial, sans-serif; color: var(--ink); }

  /* Hero */
  .hero { position: absolute; left: 0; top: 0; width: 1200px; height: 634px;
    background:
      radial-gradient(ellipse 260px 340px at 830px 420px, rgba(196,128,62,.45), transparent 70%),
      radial-gradient(ellipse 220px 380px at 430px 380px, rgba(48,92,170,.55), transparent 70%),
      linear-gradient(180deg, #15161f 0%, #1f2638 45%, #2a2f3d 80%, #3a3128 100%); }
  .brand { position: absolute; left: 99px; top: 44px; font-family: "Roboto Condensed", sans-serif; font-weight: 700; font-size: 26px; color: var(--white); letter-spacing: .3px; }
  .top-contact { position: absolute; top: 22px; display: flex; align-items: center; gap: 8px; font-family: "Roboto", sans-serif; font-size: 15px; color: var(--white); }
  .top-contact .ring { width: 30px; height: 30px; border: 2px solid var(--white); border-radius: 50%; display: flex; align-items: center; justify-content: center; }
  .top-email { left: 723px; }
  .top-phone { left: 971px; }
  .main-nav { position: absolute; top: 86px; left: 0; width: 1200px; font-family: "Roboto", sans-serif; font-weight: 500; font-size: 15px; color: var(--white); }
  .main-nav a { position: absolute; color: inherit; text-decoration: none; white-space: nowrap; }
  .hero-title { position: absolute; top: 230px; width: 1200px; text-align: center; font-family: "Lato", sans-serif; font-weight: 700; font-size: 53px; color: var(--white); letter-spacing: 1px; }
  .hero-text { position: absolute; top: 322px; left: 250px; width: 700px; text-align: center; font-family: "Roboto", sans-serif; font-size: 15.5px; line-height: 29px; color: #e6e6e6; }
  .hero-btn { position: absolute; left: 531px; top: 428px; width: 138px; height: 55px; border: 2px solid var(--white); color: var(--white); font-family: "Roboto", sans-serif; font-weight: 500; font-size: 15px; display: flex; align-items: center; justify-content: center; }
  .slider-tab { position: absolute; left: 490px; top: 590px; width: 220px; height: 88px; background: var(--white); border-radius: 110px 110px 0 0 / 60px 60px 0 0; }
  .dots { position: absolute; top: 608px; left: 553px; display: flex; gap: 8px; }
  .dots span { width: 16px; height: 16px; border-radius: 50%; border: 2px solid var(--navy); }
  .dots span.active { background: var(--navy); }

  /* Headings */
  .section-title { position: absolute; width: 1200px; text-align: center; font-family: "Lato", sans-serif; font-weight: 700; font-size: 28px; color: var(--navy); }
  .section-rule { position: absolute; left: 560px; width: 80px; height: 2px; background: var(--navy); }

  /* About */
  .about-lead { position: absolute; top: 788px; width: 1200px; text-align: center; font-weight: 600; font-size: 15px; color: var(--ink); }
  .about-text { position: absolute; left: 150px; width: 900px; text-align: center; font-size: 12.5px; line-height: 21px; color: var(--muted); }
  .btn { position: absolute; top: 1000px; height: 43px; display: flex; align-items: center; justify-content: center; font-family: "Roboto", sans-serif; font-weight: 500; font-size: 14px; }
  .btn-solid { left: 479px; width: 113px; background: var(--navy); color: var(--white); }
  .btn-outline { left: 607px; width: 114px; border: 2px solid var(--ink); color: var(--ink); }

  /* Services */
  .services { position: absolute; left: 0; top: 1100px; width: 1200px; height: 540px;
    background: radial-gradient(ellipse 500px 160px at 300px 260px, rgba(80,130,200,.35), transparent 70%), linear-gradient(180deg, var(--band-top), var(--band-bottom)); }
  .services .section-title { color: var(--white); top: 74px; }
  .services .section-rule { background: var(--white); top: 128px; }
  .service { position: absolute; width: 460px; }
  .service svg { position: absolute; left: 0; top: 0; }
  .service h3 { position: absolute; left: 93px; top: 0; font-family: "Roboto", sans-serif; font-weight: 500; font-size: 23px; color: var(--white); }
  .service p { position: absolute; left: 93px; top: 40px; width: 352px; font-family: "Roboto", sans-serif; font-size: 12px; line-height: 21px; color: #d9e2f0; text-align: justify; }

  /* Gallery */
  .gallery { position: absolute; left: 97px; top: 1785px; width: 1006px; height: 521px; }
  .tile { position: absolute; overflow: hidden; }
  .tile-electronic { left: 0; top: 0; width: 331px; height: 521px; background: linear-gradient(180deg, #3b2251 0%, #2a1838 55%, #1e1429 100%); }
  .tile-tag { position: absolute; right: 0; bottom: 0; width: 167px; height: 52px; background: #1f3f86; clip-path: polygon(14% 0, 100% 0, 100% 100%, 0 100%); color: var(--white); font-family: "Roboto Condensed", sans-serif; font-weight: 500; font-size: 18px; display: flex; align-items: center; justify-content: flex-end; padding-right: 14px; }
  .tile-freestanding { left: 337px; top: 0; width: 332px; height: 259px; background: radial-gradient(ellipse at 50% 40%, #2f58b0, #1a347a 80%); color: var(--white); text-align: center; font-family: "Roboto Condensed", sans-serif; }
  .tile-freestanding .tile-name { position: absolute; top: 70px; width: 100%; font-weight: 500; font-size: 25px; }
  .tile-freestanding .tile-line { position: absolute; top: 116px; left: 126px; width: 80px; height: 2px; background: var(--white); }
  .tile-freestanding .tile-caption { position: absolute; top: 136px; width: 100%; font-weight: 500; font-size: 21px; }
  .tile-scoreboard { left: 674px; top: 0; width: 332px; height: 259px; background: linear-gradient(180deg, #141414, #1d1d2a 50%, #0f1a12); }
  .tile-letters { left: 337px; top: 264px; width: 332px; height: 257px; background: radial-gradient(ellipse at 50% 50%, #3a2414, #151515 80%); }
  .tile-terminal { left: 674px; top: 264px; width: 332px; height: 257px; background: linear-gradient(160deg, #c9ccd1 0%, #9ea6b2 50%, #6d7a8c 100%); }

  /* Footer */
  .footer { position: absolute; left: 0; top: 2383px; width: 1200px; height: 412px; background: var(--footer-bg); border-top: 3px solid var(--navy); }
  .footer-brand { position: absolute; left: 99px; top: 70px; font-family: "Roboto Condensed", sans-serif; font-weight: 700; font-size: 26px; color: var(--navy); }
  .footer-text { position: absolute; left: 99px; top: 124px; width: 642px; font-size: 13.2px; line-height: 25px; color: var(--ink); text-align: justify; }
  .social { position: absolute; left: 99px; top: 250px; display: flex; gap: 6px; }
  .social span { width: 41px; height: 41px; border: 1.5px solid #222; border-radius: 50%; }
  .contact-title { position: absolute; left: 825px; top: 36px; font-family: "Lato", sans-serif; font-weight: 700; font-size: 23px; color: var(--navy); }
  .contact-rule { position: absolute; left: 825px; top: 72px; width: 94px; height: 2px; background: var(--navy); }
  .contact-item { position: absolute; left: 827px; display: flex; align-items: center; gap: 22px; font-size: 15.5px; line-height: 24px; color: var(--ink); }
  .contact-item .badge { width: 48px; height: 48px; border-radius: 50%; background: var(--navy-deep); display: flex; align-items: center; justify-content: center; flex-shrink: 0; }
  .contact-item .badge.ring { background: transparent; border: 2px solid var(--navy-deep); }
  .footer-rule { position: absolute; left: 99px; top: 343px; width: 1002px; height: 1px; background: var(--rule); }
  .copyright { position: absolute; top: 364px; width: 1200px; text-align: center; font-weight: 600; font-size: 13px; color: var(--ink); }
</style>
</head>
<body>

<header class="hero" role="img" aria-label="Night photograph of illuminated city towers looking upward">
  <div class="brand">COASTAL BANNER BRIDGE</div>
  <div class="top-contact top-email">
    <span class="ring"><svg width="14" height="11" viewBox="0 0 14 11"><rect x="0.8" y="0.8" width="12.4" height="9.4" rx="1" fill="none" stroke="#fff" stroke-width="1.5"/><path d="M1 1.5 L7 6 L13 1.5" fill="none" stroke="#fff" stroke-width="1.5"/></svg></span>
    info@coastalbannerbridge.com
  </div>
  <div class="top-contact top-phone">
    <span class="ring"><svg width="14" height="14" viewBox="0 0 24 24"><path d="M6.6 10.8a15 15 0 0 0 6.6 6.6l2.2-2.2a1 1 0 0 1 1-.25 11.4 11.4 0 0 0 3.6.6 1 1 0 0 1 1 1V20a1 1 0 0 1-1 1A17 17 0 0 1 3 4a1 1 0 0 1 1-1h3.5a1 1 0 0 1 1 1c0 1.25.2 2.45.6 3.6a1 1 0 0 1-.25 1z" fill="#fff"/></svg></span>
    180 046 7712
  </div>
  <nav class="main-nav">
    <a style="left:443px">HOME</a>
    <a style="left:533px">ABOUT US</a>
    <a style="left:652px">SERVICES</a>
    <a style="left:768px">OUR PRODUCTS</a>
    <a style="left:924px">BLOG</a>
    <a style="left:1008px">CONTACT US</a>
  </nav>
  <h1 class="hero-title">COASTAL BANNER BRIDGE</h1>
  <p class="hero-text">Products we offer are electronic signs, illuminated channel letters, non-illuminated flat cut and molded letters, specialty products, Wayfinding.</p>
  <a class="hero-btn">READ MORE</a>
</header>
<div class="slider-tab"></div>
<div class="dots"><span class="active"></span><span></span><span></span><span></span><span></span></div>

<section class="about">
  <h2 class="section-title" style="top:701px">ABOUT COASTAL BANNER BRIDGE</h2>
  <div class="section-rule" style="top:755px"></div>
  <p class="about-lead">Our services include surveys, permits, installations and maintenance in Canada.</p>
  <p class="about-text" style="top:832px">Products we offer are electronic signs, illuminated channel letters, non-illuminated flat cut and molded letters, specialty products, Wayfinding, large format digital printing, volume printing, programs, rebranding, illuminated cabinet type signs and illuminated freestanding signs.</p>
  <p class="about-text" style="top:898px">Nemo enim ipsam voluptatem quia voluptas sit aspernatur aut odit aut fugit, sed quia consequuntur magni dolores eos qui ratione voluptatem sequi nesciunt. Neque porro quisquam est, qui dolorem ipsum quia dolor sit amet, consectetur, adipisci velit, sed quia non numquam eius modi tempora incidunt ut labore et dolore magnam aliquam quaerat voluptatem.</p>
  <a class="btn btn-solid">Read More</a>
  <a class="btn btn-outline">Contact Us</a>
</section>

<section class="services" role="img" aria-label="Deep blue tinted harbour skyline at dusk behind the services list">
  <h2 class="section-title">OUR SERVICES</h2>
  <div class="section-rule"></div>

  <div class="service" style="left:112px; top:212px">
    <svg width="64" height="74" viewBox="0 0 64 74"><rect x="6" y="8" width="52" height="62" rx="6" fill="none" stroke="#fff" stroke-width="4"/><rect x="20" y="2" width="24" height="12" rx="3" fill="#fff"/><circle cx="20" cy="32" r="7" fill="none" stroke="#fff" stroke-width="3"/><path d="M16.5 32l2.5 2.5 5-5" fill="none" stroke="#fff" stroke-width="2.5"/><circle cx="20" cy="52" r="7" fill="none" stroke="#fff" stroke-width="3"/><path d="M16.5 52l2.5 2.5 5-5" fill="none" stroke="#fff" stroke-width="2.5"/><rect x="32" y="30" width="18" height="4" fill="#fff"/><rect x="32" y="50" width="18" height="4" fill="#fff"/></svg>
    <h3>Surveys</h3>
    <p>Nemo enim ipsam voluptatem quia voluptas sit aspernatur aut odit aut fugit, sed quia consequuntur magni dolores eos qui ratione voluptatem sequi nesciunt.</p>
  </div>

  <div class="service" style="left:652px; top:212px">
    <svg width="68" height="74" viewBox="0 0 68 74"><path d="M30 4h8l1.5 7 5 2 6-4 6 6-4 6 2 5 7 1.5v8l-7 1.5-2 5" fill="none" stroke="#fff" stroke-width="5"/><path d="M30 4l-1.5 7-5 2-6-4-6 6 4 6-2 5-7 1.5v8l7 1.5 2 5-4 6 6 6 6-4" fill="none" stroke="#fff" stroke-width="5"/><circle cx="34" cy="30" r="8" fill="none" stroke="#fff" stroke-width="4"/><path d="M40 44v16h-8l14 14 14-14h-8V44z" fill="#fff"/></svg>
    <h3>Installations</h3>
    <p>Nemo enim ipsam voluptatem quia voluptas sit aspernatur aut odit aut fugit, sed quia consequuntur magni dolores eos qui ratione voluptatem sequi nesciunt.</p>
  </div>

  <div class="service" style="left:112px; top:355px">
    <svg width="64" height="70" viewBox="0 0 64 70"><rect x="30" y="2" width="32" height="24" rx="2" fill="#fff"/><rect x="36" y="8" width="20" height="3" fill="#1a4482"/><rect x="36" y="15" width="14" height="3" fill="#1a4482"/><circle cx="18" cy="14" r="7" fill="#fff"/><path d="M6 36a12 10 0 0 1 24 0v4H6z" fill="#fff"/><rect x="34" y="32" width="28" height="6" fill="#fff"/><circle cx="12" cy="48" r="6" fill="#fff"/><path d="M2 68a10 9 0 0 1 20 0z" fill="#fff"/><rect x="30" y="46" width="32" height="22" rx="2" fill="#fff"/></svg>
    <h3>Permits</h3>
    <p>Nemo enim ipsam voluptatem quia voluptas sit aspernatur aut odit aut fugit, sed quia consequuntur magni dolores eos qui ratione voluptatem sequi nesciunt.</p>
  </div>

  <div class="service" style="left:652px; top:355px">
    <svg width="68" height="70" viewBox="0 0 68 70"><circle cx="32" cy="34" r="20" fill="none" stroke="#fff" stroke-width="7" stroke-dasharray="8 5"/><circle cx="32" cy="34" r="13" fill="none" stroke="#fff" stroke-width="5"/><path d="M18 56l22-22" stroke="#fff" stroke-width="7" stroke-linecap="round"/><path d="M44 22a9 9 0 1 1 8 12l-6-6z" fill="#fff"/></svg>
    <h3>Maintenance</h3>
    <p>Nemo enim ipsam voluptatem quia voluptas sit aspernatur aut odit aut fugit, sed quia consequuntur magni dolores eos qui ratione voluptatem sequi nesciunt.</p>
  </div>
</section>

<section class="gallery-section">
  <h2 class="section-title" style="top:1688px">OUR GALLERY</h2>
  <div class="section-rule" style="top:1741px"></div>
  <div class="gallery">
    <div class="tile tile-electronic" role="img" aria-label="Vintage marquee billboard framed with bulb lights and a lit alphabet">
      <div class="tile-tag">ELECTRONIC SIGNS</div>
    </div>
    <div class="tile tile-freestanding" role="img" aria-label="Blue glowing neon backdrop for illuminated freestanding signs">
      <div class="tile-name">COASTAL BANNER BRIDGE</div>
      <div class="tile-line"></div>
      <div class="tile-caption">Illuminated Freestanding Signs</div>
    </div>
    <div class="tile tile-scoreboard" role="img" aria-label="Digital scoreboard and currency display panels"></div>
    <div class="tile tile-letters" role="img" aria-label="Orange dot matrix alphabet on a dark board"></div>
    <div class="tile tile-terminal" role="img" aria-label="Hanging wayfinding sign in an airport terminal"></div>
  </div>
</section>

<footer class="footer">
  <div class="footer-brand">COASTAL BANNER BRIDGE</div>
  <p class="footer-text">Nemo enim ipsam voluptatem quia voluptas sit aspernatur aut odit aut fugit, sed quia consequuntur magni dolores eos qui ratione voluptatem sequi nesciunt. Neque porro quisquam est, qui dolorem ipsum quia dolor sit amet, consectetur, adipisci velit, sed quia non numquam eius modi tempora incidunt ut labore et dolore magnam aliquam quaerat voluptatem.</p>
  <div class="social"><span></span><span></span><span></span><span></span></div>

  <h3 class="contact-title">Contact Us</h3>
  <div class="contact-rule"></div>
  <div class="contact-item" style="top:102px">
    <span class="badge ring"><svg width="18" height="14" viewBox="0 0 18 14"><rect width="18" height="14" rx="2" fill="#0f2f60"/><path d="M1.5 2 L9 7.5 L16.5 2" fill="none" stroke="#f1f1f1" stroke-width="1.6"/></svg></span>
    info@coastalbannerbridge.com
  </div>
  <div class="contact-item" style="top:172px">
    <span class="badge"><svg width="16" height="22" viewBox="0 0 16 22"><path d="M8 1a7 7 0 0 0-7 7c0 5 7 13 7 13s7-8 7-13a7 7 0 0 0-7-7z" fill="none" stroke="#fff" stroke-width="1.8"/><circle cx="8" cy="8" r="2.5" fill="#fff"/></svg></span>
    <span>48 Harbour Rd,<br>Canada, 67890</span>
  </div>
  <div class="contact-item" style="top:259px">
    <span class="badge ring"><svg width="20" height="20" viewBox="0 0 24 24"><path d="M6.6 10.8a15 15 0 0 0 6.6 6.6l2.2-2.2a1 1 0 0 1 1-.25 11.4 11.4 0 0 0 3.6.6 1 1 0 0 1 1 1V20a1 1 0 0 1-1 1A17 17 0 0 1 3 4a1 1 0 0 1 1-1h3.5a1 1 0 0 1 1 1c0 1.25.2 2.45.6 3.6a1 1 0 0 1-.25 1z" fill="none" stroke="#0f2f60" stroke-width="1.8"/></svg></span>
    180 046 7712
  </div>

  <div class="footer-rule"></div>
  <p class="copyright">Copyright © 2017 Coastal Banner Bridge. All rights reserved</p>
</footer>

</body>
</html>
```